Tessellaria

Club flyer, grand opening night, house/electronic music, looking for clean design with a sample image attached. Please look at the prior flyers to get an idea of the style. Guaranteed project
I would like to use the red design if possible (tessellaria flyer attached)
Text:
TESSELLARIA
Winter House Music Monthly
Opening Night Dec 13 2013
Pellmont (use logo)
Featuring
BRAMOX (House/Garage)
(use logo with just Bramox name)
w/ resident
ORV (Driftwerk)
Free All Night
21-39 year old club with all house/electronic music. classier and grown up over gimmicky
Club

```html
<!DOCTYPE html>
<html lang="en">
<head>
<meta charset="utf-8">
<title>Tessellaria — Opening Night</title>
<link rel="stylesheet" href="https://fonts.googleapis.com/css2?family=Open+Sans:wght@400;600;800&display=swap">
<style>
  :root {
    --magenta: #e21fb8;
    --magenta-deep: #c40f8f;
    --violet: #9a2be0;
    --lavender: #f3dcff;
    --pale-yellow: #f5f2a4;
    --navy: #1c2f78;
    --white: #ffffff;
    --hot-pink: #ff2f7d;
    --crimson: #d8234d;
  }
  html, body {
    margin: 0;
    padding: 0;
    overflow: hidden;
    background: #2a0a2a;
  }
  .flyer {
    position: relative;
    width: 851px;
    height: 1200px;
    overflow: hidden;
    font-family: "Open Sans", Arial, sans-serif;
    background:
      radial-gradient(ellipse 45% 30% at 62% 38%, rgba(255,255,255,0.55), rgba(255,255,255,0) 70%),
      radial-gradient(ellipse 70% 40% at 50% 35%, rgba(170,90,255,0.6), rgba(170,90,255,0) 75%),
      linear-gradient(180deg, #d52fd6 0%, var(--magenta) 30%, #e236c8 55%, var(--magenta-deep) 100%);
  }
  .title {
    position: absolute;
    top: 22px;
    left: 0;
    width: 100%;
    margin: 0;
    text-align: center;
    font-weight: 600;
    font-size: 38px;
    letter-spacing: 1px;
    color: var(--lavender);
  }
  .title-rule {
    position: absolute;
    top: 86px;
    left: 70px;
    width: 710px;
    height: 2px;
    background: linear-gradient(90deg, rgba(255,255,255,0), rgba(255,230,255,0.9) 20%, rgba(255,230,255,0.9) 80%, rgba(255,255,255,0));
  }
  .event-info {
    position: absolute;
    top: 106px;
    left: 69px;
    margin: 0;
    font-size: 28px;
    line-height: 36px;
    color: var(--pale-yellow);
    text-transform: uppercase;
  }
  .lineup {
    position: absolute;
    top: 106px;
    right: 57px;
    text-align: right;
    color: var(--white);
    text-transform: uppercase;
  }
  .lineup-label {
    margin: 0;
    font-size: 28px;
    line-height: 36px;
  }
  .headliner {
    margin: 0;
    font-weight: 800;
    font-size: 70px;
    line-height: 74px;
    letter-spacing: 2px;
    color: var(--navy);
  }
  .resident {
    margin: 0;
    font-size: 28px;
    line-height: 36px;
  }
  .resident strong {
    font-weight: 600;
    font-size: 32px;
  }
  .collective {
    position: absolute;
    top: 262px;
    right: 55px;
    margin: 0;
    font-size: 38px;
    font-weight: 400;
    letter-spacing: 12px;
    color: var(--navy);
    text-transform: uppercase;
  }
  .centrepiece {
    position: absolute;
    left: 190px;
    top: 300px;
    width: 420px;
    height: 420px;
    border-radius: 50%;
    background: radial-gradient(circle, #c4124a 0%, var(--crimson) 22%, var(--hot-pink) 45%, rgba(255,60,140,0.45) 65%, rgba(255,60,140,0) 75%);
  }
  .dance-floor {
    position: absolute;
    left: 0;
    top: 720px;
    width: 851px;
    height: 480px;
    background:
      radial-gradient(ellipse 60% 25% at 50% 5%, rgba(140,120,255,0.55), rgba(140,120,255,0) 80%),
      linear-gradient(180deg, rgba(200,120,255,0.25) 0%, rgba(255,80,180,0.55) 35%, rgba(255,70,150,0.75) 100%);
  }
  .venue {
    position: absolute;
    left: 160px;
    top: 880px;
    width: 530px;
    height: 130px;
    display: flex;
    align-items: center;
    justify-content: center;
    gap: 22px;
  }
  .venue-mark {
    width: 26px;
    height: 26px;
    background: var(--crimson);
  }
  .venue-name {
    margin: 0;
    font-size: 60px;
    font-weight: 600;
    letter-spacing: 2px;
    color: var(--crimson);
    text-transform: uppercase;
  }
  .admission {
    position: absolute;
    right: 60px;
    bottom: 18px;
    margin: 0;
    font-size: 26px;
    color: var(--white);
    text-transform: uppercase;
  }
</style>
</head>
<body>
  <main class="flyer">
    <h1 class="title">TESSELLARIA</h1>
    <div class="title-rule"></div>

    <p class="event-info">Opening Night<br>13.12.2013<br>Winter House<br>Music Monthly</p>

    <div class="lineup">
      <p class="lineup-label">Featuring</p>
      <p class="headliner">BRAMOX</p>
      <p class="resident">With <strong>ORV</strong></p>
    </div>
    <p class="collective">Driftwerk</p>

    <div class="centrepiece" role="img" aria-label="Red kaleidoscopic starburst bloom glowing at the centre of the flyer"></div>

    <div class="dance-floor" role="img" aria-label="Glowing dotted light floor in pink and violet receding into the distance"></div>

    <div class="venue">
      <span class="venue-mark"></span>
      <p class="venue-name">Pellmont</p>
    </div>

    <p class="admission">Free All Night</p>
  </main>
</body>
</html>
```